Lumen Botanicals Label Project- Updates made to project!

Project Scope: Branding opportunity for internet based skin care line. Design coordinating label for 4 different products. Each design shall be editable in Adobe Illustrator as a template including all fonts, symbols, and guides. Submit a design for all 4 products (preferably together as it would look on a retail shelf), business card, and logo.
Cleanser: STEP 1 Label Size: 5 x 4.5 inches (w x h) CALM CLEANSER
Toner: STEP 2 Label Size: 5 x 4.5 inches (w x h) TRANQUIL TONER- A piece of each crystal sits at the bottom of each solution. It coordinates with the "Quiet Heart" of our logo.
Serum STEP 3 Label Size: Label Size: 4.25 x 2.25 ANTI-AGING SERUM
Moisturizer: STEP 4 Label Size: Label Size: 1”x7.25” MOISTURIZER
Each label needs to include:
Front:
Attractive larger sized STEP #
Logo
Product name and short description
Decorative design Symbol(s)
Back:
Area on back to say short description
Directions for use
Larger area for ingredients
Website: www.lumenbotanicals-example.com
Address of distribution
Barcode

Lumen Skin Care, an esthetician created line provides organic and natural based products for all skin types. With an emphasis on anti-aging, this simple 4- step system can be used by many including pregnant and oncology consumers. The unique thing about our line is that the toners and serums contain crystals such as amethyst and rose quarts to promote Quiet Heart as well as outer beauty. Each product is handmade with natural, quality ingredients and are 70-90% Organic.
Target Market: Women ages 30-45 years old. This demographic is on the go, and wants a simple-easy to read label, & a skin care system that addresses her concerns. Just as this consumer is mindful of her fitness and what she puts in her body, she tends to purchase environmentally friendly, and natural products. Health and wellness trends reflect this, as organic beauty products are expected to grow 74% from 2013 to 2018. She enjoys meditation and yoga, and she is curious about eastern medicine holistic healing trends.

Company Name: Lumen Skin Care
Tagline: Quiet Heart- Bright Face
Package Feel: Simple, elegant easy to read step on each product. STEP 1: AM/PM. Attractive numbering. A symbol that reflects the brand. Not necessarily a Jewel or Crystal because the name speaks for itself. Beautiful, soft, eye catching design that draws the consumer to pick it up. Clear or white label welcomed. Some color palettes provided.
Descriptive words the packaging should represent: Yoga, Zen, mystic, eye catching, healing energy, natural, quality ingredients, sophisticated, beautiful, serenity, easy to read- bold-attractive numbering on front.
Inspiration Brands: VARLA Organics- Beautiful watercolor packaging that resonates a "feeling"

Attached are pictures of the packaging, inspirational pictures, skin care lines that are attractive, ect.

Packaging SPECS:

Cleanser:
Color Clear
Size 4 oz
Material PET
Case Pack
Neck Finish 24-410
Diameter 1.58 in / 4.013 cm
Height 6 in / 15.240 cm
Label Dimensions 5x4.5
Print Dimensions 5x4.5
Print Dimensions in (diameter)

TONER BOTTLE: Same as above

SERUM BOTTLE:
Color Clear
Size 2 oz
Material PET
Neck Finish 20-410
Diameter 1.358 in / 3.449 cm
Height 3.274 in / 8.316 cm

Moisturizer:
2.3 oz
Height:53 mm
Diameter: 60 mm
Neck: 58/400

Target Market(s)

Women ages 30-45 years old. This demographic is on the go, and wants a simple-easy to read label, & a skin care system that addresses her concerns. Just as this consumer is mindful of her fitness and what she puts in her body, she tends to purchase environmentally friendly, and natural products. Health and wellness trends reflect this, as organic beauty products are expected to grow 74% from 2013 to 2018. She enjoys meditation and yoga, and she is curious about eastern medicine holistic healing trends.

Industry/Entity Type

Skin Care Product

Contact Information for Business Card

Details given upon completion.

Logo Text

Lumen Botanicals Quiet Heart- Bright Face

Requirements
Must have
• A large step number on the front. Coordinating symbols and colors. Must have a professional retail look and be easy to read.
Nice to have
• Clean, simple, eye catching packaging. Watercolor designs. Designs that inspire "feelings" www.varlaorganics-example.com

```html
<!DOCTYPE html>
<html lang="en">
<head>
<meta charset="utf-8">
<title>Lumen Skin Care – Calm Cleanser Label</title>
<link href="https://fonts.googleapis.com/css2?family=Cinzel:wght@500;600&family=EB+Garamond&family=Marcellus&display=swap" rel="stylesheet">
<style>
  :root {
    --backdrop: #f3f2f1;
    --label: #ffffff;
    --ink: #1e2224;
    --ink-soft: #3a3f42;
    --teal-mid: #6fa9ac;
    --teal-pale: #cfe3e3;
  }
  html, body {
    margin: 0;
    width: 1200px;
    height: 1000px;
    overflow: hidden;
    background: var(--backdrop);
  }
  .canvas {
    position: relative;
    width: 1200px;
    height: 1000px;
  }
  .label {
    position: absolute;
    left: 250px;
    top: 185px;
    width: 700px;
    height: 630px;
    background: var(--label);
    box-shadow: 0 2px 10px rgba(0,0,0,0.06);
    overflow: hidden;
  }
  .watercolor-area {
    position: absolute;
    left: 40px;
    right: 40px;
    top: 30px;
    height: 470px;
    background: linear-gradient(180deg, var(--teal-pale) 0%, var(--teal-mid) 50%, var(--teal-pale) 100%);
  }
  .seal {
    position: absolute;
    left: 50%;
    top: 265px;
    width: 360px;
    height: 360px;
    transform: translate(-50%, -50%);
    border-radius: 50%;
    background: var(--label);
    border: 2px solid var(--ink);
    box-sizing: border-box;
    text-align: center;
    color: var(--ink);
  }
  .brand-name {
    margin: 46px 0 0;
    font-family: "Marcellus", serif;
    font-size: 60px;
    line-height: 1;
    font-weight: 400;
  }
  .brand-rule {
    width: 54px;
    height: 1px;
    margin: 14px auto 8px;
    background: var(--ink);
  }
  .brand-sub {
    font-family: "Marcellus", serif;
    font-size: 13px;
    letter-spacing: 5px;
  }
  .product-name {
    margin: 18px 0 14px;
    font-family: "Marcellus", serif;
    font-size: 34px;
    font-weight: 400;
    letter-spacing: 0.5px;
  }
  .product-copy {
    margin: 0 auto;
    width: 262px;
    font-family: "EB Garamond", serif;
    font-size: 15px;
    line-height: 1.3;
    color: var(--ink-soft);
  }
  .step {
    position: absolute;
    left: 0;
    right: 0;
    bottom: 44px;
    text-align: center;
    color: var(--ink);
  }
  .step-number {
    font-family: "Cinzel", serif;
    font-weight: 600;
    font-size: 36px;
    letter-spacing: 1px;
    line-height: 1;
  }
  .step-volume {
    margin-top: 6px;
    font-family: "EB Garamond", serif;
    font-size: 20px;
    letter-spacing: 1px;
  }
</style>
</head>
<body>
<main class="canvas">
  <section class="label">
    <div class="watercolor-area" role="img" aria-label="Teal watercolour brushwork surrounding the product seal"></div>
    <div class="seal">
      <h1 class="brand-name">Lumen</h1>
      <div class="brand-rule"></div>
      <div class="brand-sub">SKINCARE</div>
      <h2 class="product-name">CALM CLEANSER</h2>
      <p class="product-copy">Lorem ipsum dolor sit amet, in inermis aliquando vis, an eam utinam integre reformidans. Persecuti contentiones ex vim. Eros simul in eam, adhuc maiestatis mea te, no tota omnes mediocrem est.</p>
    </div>
    <div class="step">
      <div class="step-number">STEP ONE</div>
      <div class="step-volume">4 FL OZ</div>
    </div>
  </section>
</main>
</body>
</html>
```